KT-Systems advertising flag and billboard design

I need a design for advertising flag and a design for billboard.
Information can be obtained from https://kt-sytronik.de.
Updates
Target Market(s)
IT service for companies
Requirements
Must have
- Logo, contact information and services

```html
<!DOCTYPE html>
<html lang="en">
<head>
<meta charset="utf-8">
<title>KT-Systems – Billboard</title>
<link rel="stylesheet" href="https://fonts.googleapis.com/css2?family=Open+Sans:wght@600;700&family=Archivo:wght@700&display=swap">
<style>
  :root {
    --paper: #ffffff;
    --panel: #404040;
    --accent: #5470bf;
    --ink: #111111;
    --light: #ffffff;
  }
  * { margin: 0; padding: 0; box-sizing: border-box; }
  html, body { width: 1200px; height: 801px; overflow: hidden; background: var(--paper); }
  .billboard { position: relative; width: 1200px; height: 801px; overflow: hidden; background: var(--paper); }
  .billboard__shapes { position: absolute; inset: 0; }
  .service-label {
    position: absolute; transform: translateX(-50%);
    font-family: "Archivo", Arial, sans-serif; font-weight: 700;
    font-size: 16px; line-height: 1.2; color: var(--ink);
    text-align: center; white-space: nowrap;
  }
  .brand {
    position: absolute; right: 70px; top: 190px;
    font-family: "Open Sans", Arial, sans-serif; font-weight: 700;
    font-size: 34px; letter-spacing: 1px; color: var(--light);
  }
  .headline {
    position: absolute; right: 68px; top: 245px;
    font-family: "Open Sans", Arial, sans-serif; font-weight: 700;
    font-size: 84px; line-height: 118px; color: var(--light);
    text-align: right; letter-spacing: -1px;
  }
  .headline__accent { color: var(--accent); }
  .website {
    position: absolute; right: 120px; top: 680px;
    font-family: "Open Sans", Arial, sans-serif; font-weight: 700;
    font-size: 32px; color: var(--light);
  }
</style>
</head>
<body>
<main class="billboard">
  <svg class="billboard__shapes" viewBox="0 0 1200 801" width="1200" height="801" aria-hidden="false">
    <polygon class="panel-dark" points="744,0 1200,0 1200,801 419,801" fill="var(--panel)"/>
    <polygon class="panel-stripe" points="725,0 744,0 419,801 362,801" fill="var(--accent)"/>

    <g class="service-ring__links" stroke="var(--accent)" stroke-width="2.5">
      <line x1="145" y1="247" x2="230" y2="175"/>
      <line x1="295" y1="175" x2="378" y2="233"/>
      <line x1="410" y1="285" x2="410" y2="345"/>
      <line x1="378" y1="462" x2="290" y2="535"/>
      <line x1="228" y1="540" x2="145" y2="480"/>
      <line x1="114" y1="350" x2="114" y2="418"/>
    </g>

    <g class="service-ring__nodes" fill="var(--paper)" stroke="var(--accent)" stroke-width="2.5">
      <circle cx="262" cy="160" r="28"/>
      <circle cx="410" cy="247" r="28"/>
      <circle cx="410" cy="444" r="28"/>
      <circle cx="260" cy="552" r="28"/>
      <circle cx="114" cy="460" r="28"/>
      <circle cx="114" cy="265" r="28"/>
    </g>

    <g class="service-icons" fill="none" stroke="var(--ink)" stroke-width="2.2" stroke-linecap="round" stroke-linejoin="round">
      <!-- PC -->
      <rect x="249" y="150" width="7" height="18"/>
      <rect x="259" y="150" width="16" height="11"/>
      <line x1="267" y1="161" x2="267" y2="167"/><line x1="262" y1="168" x2="272" y2="168"/>
      <!-- tick -->
      <circle cx="410" cy="247" r="11"/>
      <polyline points="404,247 409,252 418,240"/>
      <!-- backup shield -->
      <path d="M410 432 l11 4 v8 c0 7 -5 11 -11 13 c-6 -2 -11 -6 -11 -13 v-8 z"/>
      <polyline points="405,445 409,449 415,441"/>
      <!-- server -->
      <rect x="252" y="539" width="16" height="6"/>
      <rect x="252" y="547" width="16" height="6"/>
      <line x1="260" y1="553" x2="260" y2="562"/><line x1="253" y1="563" x2="267" y2="563"/>
      <!-- malware shield -->
      <path d="M116 447 l10 4 v8 c0 7 -5 11 -10 13 c-5 -2 -10 -6 -10 -13 v-8 z"/>
      <circle cx="105" cy="468" r="3"/>
      <!-- laptop -->
      <rect x="104" y="255" width="20" height="13"/>
      <line x1="100" y1="273" x2="128" y2="273"/>
    </g>

    <rect class="service-illustration" role="img" aria-label="Illustration of a technician working at a laptop"
          x="180" y="265" width="164" height="175" rx="6" fill="#2a2a2a"/>
  </svg>

  <p class="service-label" style="left:262px; top:106px;">PC Repair</p>
  <p class="service-label" style="left:410px; top:283px;">System Check</p>
  <p class="service-label" style="left:410px; top:480px;">Data Backup<br>&amp; Recovery</p>
  <p class="service-label" style="left:260px; top:588px;">Network / Servers</p>
  <p class="service-label" style="left:114px; top:496px;">Malware and<br>Virus Removing</p>
  <p class="service-label" style="left:114px; top:301px;">Laptop Repair</p>

  <p class="brand">KT-Systems</p>
  <h1 class="headline">Your partner<br>for <span class="headline__accent">IT-Services</span></h1>
  <p class="website">https://kt-sytronik.de</p>
</main>
</body>
</html>
```